VORTIQ Business Card Design

We need a business card for a new company based on the Gold Coast, we are a new supplement distributing company called VORTIQ Sports Nutrition - Bold Horizon Sports Nutrition. We are providing new science based bodybuilding and fitness supplementation. Our company has a key focus towards next generation. We are wanting a card that is cool, innovative and fresh. We would like to see the implementation of the below image in a fresh and very innovative design that stands out. The final design should communicate New, Innovative, Cool, Science and researched based.
Target Market(s)
The target market is fitness and bodybuilder enthusiasts. Young audience so very cool looking.
Industry/Entity Type
Fitness
Contact Information for Business Card
(front of card)
VORTIQ Sports Nutrition.
Milo Harrow
CEO/Sport Nutrition Specialist
0473 628 904
Milo@vortiqfuelworks.example
www.vortiqfuelworks.example
(back of card)
Scientifically formulated supplement range
Private Nutrition consultations
comprehensive sports nutrition seminars
Requirements
Nice to have
- The card could have a cut out on one of the sides or one of the corners rounded off so the card looks different from a normal business card.
Should not have
- The colours need to complement each other and pop out.

```html
<!DOCTYPE html>
<html lang="en">
<head>
<meta charset="utf-8">
<title>VORTIQ Sports Nutrition – Business Card</title>
<link rel="stylesheet" href="https://fonts.googleapis.com/css2?family=Roboto+Condensed:wght@400;700&family=Open+Sans:ital,wght@0,400;1,400&display=swap">
<style>
  :root {
    --page-bg: #eeeff0;
    --card-top: #0f3d4d;
    --card-bottom: #04121a;
    --accent: #5cc6ee;
    --text-light: #f2f6f8;
    --text-soft: #d7e3e8;
  }
  * { box-sizing: border-box; margin: 0; padding: 0; }
  html, body { width: 1200px; height: 861px; overflow: hidden; }
  body {
    background: var(--page-bg);
    font-family: "Open Sans", sans-serif;
    position: relative;
  }
  .card {
    position: absolute;
    left: 270px;
    width: 660px;
    height: 377px;
    border-radius: 30px 6px 30px 6px;
    background: linear-gradient(160deg, var(--card-top) 0%, #0a2633 45%, var(--card-bottom) 100%);
    box-shadow: 0 12px 30px rgba(0, 0, 0, 0.25);
    color: var(--text-light);
    overflow: hidden;
  }
  .card-front { top: 36px; }
  .card-back { top: 448px; }

  .brand {
    display: flex;
    align-items: center;
    gap: 12px;
  }
  .brand-dot {
    width: 34px;
    height: 34px;
    border-radius: 50%;
    background: var(--accent);
  }
  .brand-name {
    font-family: "Roboto Condensed", sans-serif;
    font-weight: 700;
    font-size: 52px;
    letter-spacing: 2px;
    color: var(--text-light);
  }
  .tagline {
    font-family: "Open Sans", sans-serif;
    font-style: italic;
    font-size: 13px;
    color: var(--text-light);
    letter-spacing: 0.3px;
  }

  /* front */
  .card-front .brand { position: absolute; left: 46px; top: 168px; }
  .card-front .tagline { position: absolute; left: 34px; top: 290px; }
  .holder {
    position: absolute;
    right: 30px;
    top: 26px;
    text-align: right;
    font-family: "Roboto Condensed", sans-serif;
    font-weight: 700;
  }
  .holder-name { font-size: 48px; color: var(--accent); line-height: 1.05; }
  .holder-role { font-size: 21px; color: var(--text-soft); line-height: 1.35; }
  .contact-list {
    position: absolute;
    right: 30px;
    top: 234px;
    list-style: none;
    text-align: right;
  }
  .contact-item {
    display: flex;
    justify-content: flex-end;
    align-items: center;
    gap: 10px;
    font-family: "Roboto Condensed", sans-serif;
    font-size: 20px;
    color: var(--text-light);
    height: 46px;
  }
  .contact-icon { width: 32px; height: 32px; flex: none; }

  /* back */
  .card-back .brand { position: absolute; left: 0; right: 0; top: 70px; justify-content: center; }
  .card-back .tagline { position: absolute; left: 0; right: 0; top: 150px; text-align: center; font-style: normal; letter-spacing: 1px; }
  .services {
    position: absolute;
    left: 0; right: 0;
    top: 220px;
    text-align: center;
    font-family: "Roboto Condensed", sans-serif;
    font-weight: 700;
    font-size: 19px;
    line-height: 1.55;
    color: var(--text-soft);
  }
</style>
</head>
<body>

<section class="card card-front" aria-label="Business card front">
  <div class="brand">
    <span class="brand-dot"></span>
    <span class="brand-name">VORTIQ</span>
  </div>
  <p class="tagline">BOLD HORIZON SPORTS NUTRITION.</p>

  <div class="holder">
    <h1 class="holder-name">Milo Harrow</h1>
    <p class="holder-role">CEO</p>
    <p class="holder-role">Sport Nutrition Specialist</p>
  </div>

  <ul class="contact-list">
    <li class="contact-item">0473 628 904
      <svg class="contact-icon" viewBox="0 0 32 32" aria-hidden="true">
        <circle cx="16" cy="16" r="14" fill="none" stroke="var(--accent)" stroke-width="2.5"/>
        <path d="M11 9 l3 0 l1.5 4 l-2 1.5 a9 9 0 0 0 4 4 l1.5 -2 l4 1.5 l0 3 a2 2 0 0 1 -2 2 a13 13 0 0 1 -12 -12 a2 2 0 0 1 2 -2z" fill="var(--accent)"/>
      </svg>
    </li>
    <li class="contact-item">Milo@vortiqfuelworks.example
      <svg class="contact-icon" viewBox="0 0 32 32" aria-hidden="true">
        <circle cx="16" cy="16" r="14" fill="none" stroke="var(--accent)" stroke-width="2.5"/>
        <rect x="8.5" y="11" width="15" height="10" fill="var(--accent)"/>
        <path d="M8.5 11 l7.5 6 l7.5 -6" fill="none" stroke="#0a2633" stroke-width="1.4"/>
      </svg>
    </li>
    <li class="contact-item">www.vortiqfuelworks.example
      <svg class="contact-icon" viewBox="0 0 32 32" aria-hidden="true">
        <circle cx="16" cy="16" r="14" fill="none" stroke="var(--accent)" stroke-width="2.5"/>
        <circle cx="16" cy="16" r="8" fill="none" stroke="var(--accent)" stroke-width="1.8"/>
        <ellipse cx="16" cy="16" rx="3.5" ry="8" fill="none" stroke="var(--accent)" stroke-width="1.5"/>
        <path d="M8 16 h16 M9.5 12 h13 M9.5 20 h13" stroke="var(--accent)" stroke-width="1.3"/>
      </svg>
    </li>
  </ul>
</section>

<section class="card card-back" aria-label="Business card back">
  <div class="brand">
    <span class="brand-dot"></span>
    <span class="brand-name">VORTIQ</span>
  </div>
  <p class="tagline">BOLD HORIZON SPORTS NUTRITION.</p>
  <div class="services">
    <p>Scientifically formulated supplement range</p>
    <p>Private Nutrition consultations comprehensive sports nutrition seminars</p>
  </div>
</section>

</body>
</html>
```